Unique and original Business Card for Financial Services Business

I have moved premises and need to change the detail on my business card so thought now is a good time for a re-design. Looking for something professional and modern with colours to fit in with out logo. Like the idea of foil or embossing if that works but not a must have but I do want something that stands out and that I could not design myself.

Once business card is designed I will also be looking to get letterhead and flyers done but want the business card concept in place first.

The majority of designs I am receiving are generic and template based. I am looking for something unique and original. We have some great design elements in our logo, think outside the box and show me something that stands out from the crowd.

Target Market(s)

Business Professionals

Industry/Entity Type

Finance

Contact Information for Business Card

Name: Delia Norwood Phone 0473 958 162 Address PO Box 8617 Mossvale NSW 2389 Email info@steadyharbourfinancialservices.com.au website www.steadyharbourfinancialservices.com.au

Font styles to use
Other font styles liked:
• Ralway

Requirements
Should not have
• No black backgrounds please

```html
<!DOCTYPE html>
<html lang="en">
<head>
<meta charset="utf-8">
<title>Steady Harbour Financial Services – Business Card</title>
<link rel="stylesheet" href="https://fonts.googleapis.com/css2?family=Raleway:wght@300;400&family=Open+Sans:wght@400;700&display=swap">
<style>
  :root {
    --bg: #e9ecee;
    --teal: #1f9a96;
    --teal-light: #2aaba2;
    --teal-dark: #033a52;
    --white: #ffffff;
    --ink: #3a4148;
    --grey: #b9bec3;
  }
  * { margin: 0; padding: 0; box-sizing: border-box; }
  html, body { width: 1200px; height: 913px; overflow: hidden; background: var(--bg); }
  .canvas { position: relative; width: 1200px; height: 913px; }

  .card {
    position: absolute;
    width: 600px;
    height: 343px;
    border-radius: 22px;
    overflow: hidden;
    box-shadow: 0 10px 30px rgba(0,0,0,0.18);
  }

  /* Front */
  .card-front {
    left: 50px; top: 50px;
    background: linear-gradient(35deg, var(--teal-dark) 0%, #0a6a75 50%, var(--teal-light) 100%);
    display: flex; align-items: center; justify-content: center;
  }
  .brand { display: flex; flex-direction: column; align-items: center; }
  .brand-mark {
    width: 62px; height: 62px; border-radius: 50%;
    margin-bottom: 16px;
  }
  .brand-name {
    font-family: 'Raleway', sans-serif; font-weight: 300;
    font-size: 40px; line-height: 1; letter-spacing: 0.5px;
  }
  .brand-sub {
    font-family: 'Raleway', sans-serif; font-weight: 300;
    font-size: 15px; letter-spacing: 7px; margin-top: 8px;
  }
  .card-front .brand-mark { background: var(--white); }
  .card-front .brand-name, .card-front .brand-sub { color: var(--white); }

  /* Back */
  .card-back { left: 560px; top: 520px; background: var(--white); }
  .card-back .brand {
    position: absolute; left: 22px; top: 96px; width: 290px;
  }
  .card-back .brand-mark { background: var(--teal); width: 50px; height: 50px; margin-bottom: 12px; }
  .card-back .brand-name { color: var(--teal); font-size: 28px; }
  .card-back .brand-sub { color: var(--teal); font-size: 11px; letter-spacing: 5px; }

  .divider {
    position: absolute; left: 322px; top: 40px;
    width: 1.5px; height: 150px; background: var(--teal);
  }
  .contact {
    position: absolute; left: 336px; top: 40px;
    font-family: 'Open Sans', sans-serif; color: var(--ink);
  }
  .contact-name {
    font-weight: 700; font-size: 19px; color: var(--teal);
    text-transform: uppercase; letter-spacing: 0.2px; line-height: 1.1;
  }
  .contact-role { font-size: 12px; margin-bottom: 10px; }
  .contact-address { font-size: 11.5px; line-height: 1.45; margin-bottom: 10px; }
  .contact-line {
    display: flex; align-items: center; gap: 5px;
    font-size: 10.2px; line-height: 1.6; letter-spacing: -0.1px;
  }
  .contact-line svg { width: 10px; height: 10px; flex: none; fill: var(--teal-dark); }

  .swoosh { position: absolute; left: 0; top: 0; width: 600px; height: 343px; }
</style>
</head>
<body>
<div class="canvas">

  <section class="card card-front">
    <div class="brand">
      <span class="brand-mark"></span>
      <div class="brand-name">STEADY HARBOUR</div>
      <div class="brand-sub">Financial Services</div>
    </div>
  </section>

  <section class="card card-back">
    <svg class="swoosh" viewBox="0 0 600 343" aria-hidden="true">
      <defs>
        <linearGradient id="wave-teal" x1="0" y1="1" x2="1" y2="0">
          <stop offset="0" stop-color="#2aaba2"/>
          <stop offset="1" stop-color="#033a52"/>
        </linearGradient>
        <linearGradient id="wave-grey" x1="0" y1="0" x2="1" y2="0">
          <stop offset="0" stop-color="#ffffff"/>
          <stop offset="0.5" stop-color="#b9bec3"/>
          <stop offset="1" stop-color="#8d949a"/>
        </linearGradient>
      </defs>
      <path d="M110,343 C240,292 440,268 600,150 L600,178 C450,292 270,312 150,343 Z" fill="url(#wave-grey)"/>
      <path d="M150,343 C270,314 450,296 600,186 L600,343 Z" fill="url(#wave-teal)"/>
    </svg>

    <div class="brand">
      <span class="brand-mark"></span>
      <div class="brand-name">STEADY HARBOUR</div>
      <div class="brand-sub">Financial Services</div>
    </div>

    <div class="divider"></div>

    <div class="contact">
      <div class="contact-name">Delia Norwood</div>
      <div class="contact-role">President</div>
      <div class="contact-address">PO Box 8617<br>Mossvale NSW 2389</div>
      <div class="contact-line">
        <svg viewBox="0 0 24 24"><path d="M6.6 10.8a15.1 15.1 0 0 0 6.6 6.6l2.2-2.2c.3-.3.7-.4 1-.2 1.1.4 2.3.6 3.6.6.6 0 1 .4 1 1V20c0 .6-.4 1-1 1A17 17 0 0 1 3 4c0-.6.4-1 1-1h3.5c.6 0 1 .4 1 1 0 1.3.2 2.5.6 3.6.1.3 0 .7-.2 1z"/></svg>
        <span>0473 958 162</span>
      </div>
      <div class="contact-line">
        <svg viewBox="0 0 24 24"><path d="M2 5h20v14H2z M2 5l10 8 10-8" /></svg>
        <span>info@steadyharbourfinancialservices.com.au</span>
      </div>
      <div class="contact-line">
        <svg viewBox="0 0 24 24"><circle cx="12" cy="12" r="10"/></svg>
        <span>www.steadyharbourfinancialservices.com.au</span>
      </div>
    </div>
  </section>

</div>
</body>
</html>
```